Webbanner-Design für Blog gesucht
Zielgruppe
Es geht um ein privates Blog. Inhalte des Blogs werden Gedanken zu Zitaten (aus Büchern, Film, Kino, Altertum, usw), Sprichwörtern, Gedichten usw sein. Der Titel des Blogs wird 'sinnverwebt' sein. Es wird teils nachdenklich, teils humorvoll zugehen. Technische Basis: Wordpress
Aufgabenstellung
Der Banner soll oben eingebunden werden, und soll den Begriff 'Sinnverwebt' enthalten.

```html
<!DOCTYPE html>
<html lang="de">
<head>
<meta charset="utf-8">
<title>Sinnverwebt – Banner-Entwürfe</title>
<link rel="stylesheet" href="https://fonts.googleapis.com/css2?family=Source+Sans+3:wght@300;400&display=swap">
<style>
  :root {
    --page: #ffffff;
    --wall-light: #f7f6f5;
    --wall-mid: #ebeae8;
    --floor: #e4e0da;
    --wall-grey: #e6e6e6;
    --wall-grey-dark: #d4d4d4;
    --floor-dark: #5a5a5a;
    --title-light: #8a8a8a;
    --title-dark: #616161;
    --scene-pink: #d94fbf;
    --scene-teal: #6cc4d8;
    --scene-yellow: #d8d84a;
  }
  html, body {
    margin: 0;
    padding: 0;
    width: 1200px;
    height: 849px;
    overflow: hidden;
    background: var(--page);
  }
  .sheet {
    position: relative;
    width: 1200px;
    height: 849px;
  }
  .banner {
    position: absolute;
    left: 244px;
    width: 712px;
    height: 238px;
    overflow: hidden;
  }
  .banner--caps { top: 144px; }
  .banner--mixed { top: 478px; }
  .banner svg { display: block; }
  .banner__title {
    position: absolute;
    margin: 0;
    white-space: nowrap;
    font-family: "Source Sans 3", sans-serif;
    line-height: 1;
  }
  .banner--caps .banner__title {
    left: 36px;
    top: 108px;
    font-size: 64px;
    font-weight: 300;
    letter-spacing: 0.5px;
    color: var(--title-light);
  }
  .banner--mixed .banner__title {
    left: 67px;
    top: 85px;
    font-size: 62px;
    font-weight: 400;
    color: var(--title-dark);
  }
</style>
</head>
<body>
<main class="sheet">

  <section class="banner banner--caps">
    <svg width="712" height="238" viewBox="0 0 712 238" role="img" aria-label="Heller leerer Raum mit weißer Wand und Holzboden, eine offene Tür, aus der bunte Fragezeichen auf den Boden fallen">
      <defs>
        <linearGradient id="capsWall" x1="0" y1="0" x2="1" y2="0">
          <stop offset="0" stop-color="var(--wall-mid)"/>
          <stop offset="1" stop-color="var(--wall-light)"/>
        </linearGradient>
        <linearGradient id="capsScene" x1="0" y1="0" x2="1" y2="1">
          <stop offset="0" stop-color="var(--scene-pink)" stop-opacity="0.55"/>
          <stop offset="0.5" stop-color="var(--scene-teal)" stop-opacity="0.55"/>
          <stop offset="1" stop-color="var(--scene-yellow)" stop-opacity="0.55"/>
        </linearGradient>
      </defs>
      <rect width="712" height="163" fill="url(#capsWall)"/>
      <rect y="163" width="712" height="75" fill="var(--floor)"/>
      <rect x="427" y="16" width="220" height="202" rx="12" fill="url(#capsScene)"/>
    </svg>
    <h1 class="banner__title">SINNVERWEBT</h1>
  </section>

  <section class="banner banner--mixed">
    <svg width="712" height="238" viewBox="0 0 712 238" role="img" aria-label="Schräge Raumecke mit heller Wand und dunklem Boden, eine offene Tür, aus der bunte Fragezeichen quellen">
      <defs>
        <linearGradient id="mixedWall" x1="0" y1="0" x2="1" y2="1">
          <stop offset="0" stop-color="var(--wall-grey)"/>
          <stop offset="1" stop-color="var(--wall-grey-dark)"/>
        </linearGradient>
        <linearGradient id="mixedScene" x1="0" y1="0" x2="1" y2="1">
          <stop offset="0" stop-color="var(--scene-pink)" stop-opacity="0.6"/>
          <stop offset="0.5" stop-color="var(--scene-teal)" stop-opacity="0.6"/>
          <stop offset="1" stop-color="var(--scene-yellow)" stop-opacity="0.6"/>
        </linearGradient>
      </defs>
      <rect width="712" height="238" fill="url(#mixedWall)"/>
      <polygon points="625,0 712,0 712,238 386,238" fill="var(--floor-dark)"/>
      <line x1="625" y1="0" x2="386" y2="238" stroke="#f4f4f4" stroke-width="3"/>
      <rect x="451" y="15" width="184" height="202" rx="12" fill="url(#mixedScene)"/>
    </svg>
    <h1 class="banner__title">Sinnverwebt</h1>
  </section>

</main>
</body>
</html>
```